依頼詳細
■依頼目的
本ブログの目的は、ミラボルト テクノサービスの認知拡大とブランディングとなります。
MTSの技術や最新動向への見解・取組を掲載する「MTS Tech ブログ」を立ち上げ、
中途採用 転職意向者 / ソリューション導入 検討者の意向を上げることを狙っております。

■デザインイメージ
ソラノート社運営ブログ「Buildnote.JX」
http://dev.soranote-example.jp/
制作注意点としまして、実装にはWordPressを使いますのでWordPressで実装が明らかにできないような
デザインは避けてください

■訴求ポイントの優先順位
1.ブログスペース
2.求人広告バナーエリア(自社のキャリア採用)

■ターゲット層
個人:中途採用 転職意向者
法人:ソリューション導入 検討者

■希望する色味
ミラボルトテクノサービスのトーン&マナーに合わせたもの
http://www.mts.mirabolt-example.co.jp/

■提供素材
ミラボルトテクノサービス:ロゴデーター

■納品ファイル
TOPページデザイン1点(PSDデータ)
ロゴの使用につきましては、添付のレギュレーションに従って作成をお願い致します。
デザインコンセプトにつきまして補足をさせて頂きます。TOPページのイメージとしまして一般的なブログ形式ではなく、デザインとレイアウトに関しましては最近のビジネスブログやキュレーションメディアのトレンドも考慮した先進性のあるデザインを考慮し、なおかつ読みやすい体裁での設計をお願いいたします。皆様からのご提案を心よりお待ちしております。よろしくお願いいたします。
ランサー様各位
この度は、たくさんの素晴らしいご提案を頂きましてありがとうございます。
さらにより多くの方からの魅力的なご応募を頂けるのではと思いまして
一週間延長の3/11(水)に延長することといたしました。
引き続き皆様からのご提案をお待ち申し上げます。

サイトの性質上、どうしても縦に長くなる中で、背景色に変化をつけることにより、情報ごとのブロックの認識がわかりやすくなったと感じます。また、単純なグリッドデザインでなくなり、変化がついていたところが決定したポイントになります。

この度は、皆様に当コンペにたくさんの素晴らしいデザインをご提案して頂きましてありがとうございました。

```html
<!DOCTYPE html>
<html lang="ja">
<head>
<meta charset="utf-8">
<title>MTS 技術ブログ</title>
<link href="https://fonts.googleapis.com/css2?family=Noto+Sans+JP:wght@400;500;700;900&display=swap" rel="stylesheet">
<style>
:root{
  --navy:#1d2a5c;
  --blue:#3f7cc4;
  --blue-dark:#2f64a8;
  --teal:#3cc2b2;
  --grey-bg:#e4e5e7;
  --line:#d5d7db;
  --text:#2b2b2b;
  --muted:#777;
  --tag-client:#2db3c4;
  --tag-intro:#f08a24;
  --tag-db:#2f6db5;
  --tag-server:#e2452c;
  --white:#fff;
}
*{box-sizing:border-box;margin:0;padding:0}
html,body{width:1200px;height:2400px;overflow:hidden}
body{font-family:"Noto Sans JP",sans-serif;color:var(--text);background:var(--white);position:relative}
ul{list-style:none}

/* header */
.site-header{height:76px;display:flex;align-items:center;padding:0 60px;justify-content:space-between}
.brand{display:flex;align-items:center;gap:12px}
.brand-mark{width:22px;height:22px;background:var(--navy)}
.brand-name{font-weight:700;font-size:15px;color:var(--navy);line-height:1.1;width:110px}
.site-title{font-weight:700;font-size:26px;color:var(--navy);margin-left:14px;letter-spacing:1px}
.global-nav{display:flex;align-items:center;gap:26px;font-weight:700;font-size:18px;color:var(--navy);letter-spacing:1px}
.feed-icon{width:22px;height:22px}

/* hero */
.hero{height:184px;display:flex;gap:20px;background:#dcdde0}
.hero-slide{flex:1;position:relative;overflow:hidden}
.hero-photo{position:absolute;inset:0}
.hero-slide .caption{position:absolute;left:28px;bottom:30px;color:var(--white);font-weight:700;font-size:24px;line-height:1.25;text-shadow:0 1px 3px rgba(0,0,0,.4)}
.hero-slide.is-center{background:var(--navy);display:flex;align-items:center;justify-content:center;gap:16px}
.hero-slide.is-center .brand-mark{background:var(--white);width:34px;height:34px}
.hero-slide.is-center .brand-name{color:var(--white);font-size:26px;width:auto}
.hero-slide.is-right .caption{left:auto;right:40px;bottom:auto;top:50px;text-align:left}

/* category nav */
.category-nav{height:52px;background:var(--blue);display:flex;margin-top:8px}
.category-nav li{flex:1;display:flex;align-items:center;justify-content:center;color:var(--white);font-weight:700;font-size:18px;border-right:1px solid rgba(255,255,255,.25);position:relative}
.category-nav li.is-active{background:var(--teal)}
.category-nav li.is-active::after{content:"";position:absolute;bottom:-10px;left:50%;margin-left:-10px;border:10px solid transparent;border-bottom:0;border-top-color:var(--teal)}

/* popular */
.popular{padding:16px 60px 0;height:400px}
.popular-label{font-size:12px;color:var(--muted);border-bottom:1px solid var(--line);padding-bottom:4px}
.popular-list{display:flex;gap:18px;margin-top:8px}
.popular-item{flex:1}
.popular-item time{display:block;font-size:13px;color:var(--muted);margin-bottom:4px}
.popular-thumb{height:196px}
.popular-item h3{font-size:15px;font-weight:500;margin-top:10px;line-height:1.45}

/* content */
.content{position:absolute;top:660px;left:0;width:1200px;height:1580px;background:var(--grey-bg);padding:20px 80px 0;display:flex;gap:30px}
.main{width:680px}
.section-label{background:#cfd1d5;color:#555;font-size:13px;padding:5px 12px;margin-bottom:14px}
.article-list{display:flex;flex-direction:column;gap:16px}
.article-card{height:218px;background:var(--white);display:flex}
.article-thumb{width:270px;position:relative;flex-shrink:0}
.article-thumb .photo{position:absolute;inset:0 0 30px 0;background:linear-gradient(135deg,#5a5a5a,#1e1e1e 65%)}
.tag{position:absolute;left:0;right:0;bottom:0;height:30px;color:var(--white);font-size:13px;font-weight:700;display:flex;align-items:center;justify-content:center}
.tag.client{background:var(--tag-client)}
.tag.intro{background:var(--tag-intro)}
.tag.db{background:var(--tag-db)}
.tag.server{background:var(--tag-server)}
.article-body{padding:24px 26px}
.article-body time{display:block;text-align:right;font-size:15px;color:var(--muted)}
.article-body h2{font-size:27px;font-weight:900;margin-top:6px;line-height:1.25}
.article-body p{font-size:13px;color:#555;line-height:1.6;margin-top:12px}
.more-button{display:flex;align-items:center;justify-content:center;height:48px;margin-top:30px;background:var(--blue-dark);color:var(--white);font-weight:700;font-size:18px}

/* sidebar */
.sidebar{width:330px}
.recruit-banner{height:312px;background:var(--navy);display:flex;flex-direction:column}
.recruit-banner .logo-area{flex:1;display:flex;align-items:center;justify-content:center;gap:14px}
.recruit-banner .brand-mark{background:var(--white);width:30px;height:30px}
.recruit-banner .brand-name{color:var(--white);font-size:22px;width:auto}
.recruit-banner .cta{height:74px;border-top:2px solid rgba(255,255,255,.6);display:flex;align-items:center;justify-content:center;color:var(--white);font-weight:700;font-size:22px;margin:0 20px}
.pickup{margin-top:40px;background:var(--white);padding:16px 18px 18px}
.pickup-title{display:flex;align-items:center;justify-content:center;gap:10px;font-weight:900;font-size:20px;color:var(--navy);margin-bottom:12px}
.pickup-title i{width:9px;height:9px;background:var(--teal);transform:rotate(45deg)}
.pickup-item{display:flex;gap:12px;align-items:center;margin-top:10px}
.pickup-thumb{width:84px;height:50px;flex-shrink:0;background:linear-gradient(135deg,#2f9c66,#c9c42f)}
.pickup-item span{font-size:13px;line-height:1.4}
.categories{margin-top:24px;background:var(--white);padding:18px 22px;height:266px}
.categories h4{text-align:center;font-size:17px;font-weight:700;color:var(--navy);margin-bottom:14px}
.categories li{font-size:14px;color:var(--blue-dark);line-height:1.75;border-bottom:1px dotted var(--line)}
.search{margin-top:24px;display:flex;height:50px}
.search .field{flex:1;background:var(--white);border:1px solid var(--line)}
.search .button{width:50px;background:var(--blue-dark);display:flex;align-items:center;justify-content:center}

/* footer */
.site-footer{position:absolute;top:2240px;left:0;width:1200px;height:160px;background:var(--navy);display:flex;align-items:center;padding:0 80px;justify-content:space-between}
.site-footer .brand-mark{background:var(--white);width:28px;height:28px}
.site-footer .brand-name{color:var(--white);font-size:20px;width:auto}
.footer-nav{display:flex;gap:80px;color:var(--white);font-weight:700;font-size:20px;letter-spacing:1px}
</style>
</head>
<body>

<header class="site-header">
  <div class="brand">
    <span class="brand-mark"></span>
    <span class="brand-name">ミラボルト テクノサービス</span>
    <h1 class="site-title">MTS 技術ブログ</h1>
  </div>
  <nav class="global-nav">
    <span>MENU</span><span>MENU</span><span>MENU</span>
    <svg class="feed-icon" viewBox="0 0 22 22"><circle cx="4" cy="18" r="3" fill="#1d2a5c"/><path d="M2 9a11 11 0 0 1 11 11" stroke="#1d2a5c" stroke-width="3" fill="none"/><path d="M2 2a18 18 0 0 1 18 18" stroke="#1d2a5c" stroke-width="3" fill="none"/></svg>
  </nav>
</header>

<section class="hero">
  <div class="hero-slide">
    <div class="hero-photo" role="img" aria-label="カンファレンス会場の写真" style="background:linear-gradient(135deg,#9aa3ad,#4b525b)"></div>
    <p class="caption">Tech Summit 2015<br>レポート</p>
  </div>
  <div class="hero-slide is-center">
    <span class="brand-mark"></span>
    <span class="brand-name">ミラボルト テクノサービス</span>
  </div>
  <div class="hero-slide is-right">
    <div class="hero-photo" role="img" aria-label="ノートパソコンで作業する手元の写真" style="background:linear-gradient(135deg,#b9c2cc,#6f7b88)"></div>
    <p class="caption">Webサイト<br>パフォーマンス</p>
  </div>
</section>

<nav>
  <ul class="category-nav">
    <li>入門</li>
    <li>クライアントサイド</li>
    <li class="is-active">サーバーサイド</li>
    <li>DB</li>
    <li>HTML/CSS</li>
  </ul>
</nav>

<section class="popular">
  <p class="popular-label">サーバーサイドの人気記事</p>
  <ul class="popular-list">
    <li class="popular-item"><time>2014.4.21</time><div class="popular-thumb" role="img" aria-label="負荷分散を表すアイコンのイラスト" style="background:linear-gradient(135deg,#2e2e2e,#4a4a3a)"></div><h3>パフォーマンス改善！負荷分散をはじめよう</h3></li>
    <li class="popular-item"><time>2014.4.21</time><div class="popular-thumb" role="img" aria-label="クラウドアップロードのアイコンのイラスト" style="background:#d9739a"></div><h3>自動化だけで簡単アップロード！SoraUpload</h3></li>
    <li class="popular-item"><time>2014.4.21</time><div class="popular-thumb" role="img" aria-label="新ツールのロゴ風イラスト" style="background:#cfe6f2"></div><h3>ついに正式リリース！期待の新ツールでできること</h3></li>
    <li class="popular-item"><time>2014.4.21</time><div class="popular-thumb" role="img" aria-label="2015年のおすすめサービスを表す写真" style="background:linear-gradient(135deg,#5a5a5a,#1e1e1e)"></div><h3>2015おすすめサービス</h3></li>
    <li class="popular-item"><time>2014.4.21</time><div class="popular-thumb" role="img" aria-label="デスクの写真" style="background:linear-gradient(135deg,#6a6a6a,#2a2a2a)"></div><h3>2015おすすめサービス</h3></li>
  </ul>
</section>

<div class="content">
  <main class="main">
    <p class="section-label">新着記事</p>
    <div class="article-list">
      <article class="article-card"><div class="article-thumb"><div class="photo" role="img" aria-label="2015年のサービスを表す写真"></div><span class="tag client">クライアントサイド</span></div>
        <div class="article-body"><time>2014.4.21</time><h2>2015年おすすめサービスまとめ</h2><p>こんにちはクライアントサイド担当Bです。今日は私的に気になるサービスについてまとめてみました。作業効率が劇的に改善したサービス…</p></div></article>
      <article class="article-card"><div class="article-thumb"><div class="photo" role="img" aria-label="2015年のサービスを表す写真"></div><span class="tag intro">入門</span></div>
        <div class="article-body"><time>2014.4.21</time><h2>パフォーマンス改善！負荷分散をはじめよう</h2><p>こんにちはクライアントサイド担当Bです。今日は私的に気になるサービスについてまとめてみました。</p></div></article>
      <article class="article-card"><div class="article-thumb"><div class="photo" role="img" aria-label="2015年のサービスを表す写真"></div><span class="tag db">DB</span></div>
        <div class="article-body"><time>2014.4.21</time><h2>2015年おすすめサービスまとめ</h2><p>こんにちはクライアントサイド担当Bです。今日は私的に気になるサービスについてまとめてみました。作業効率が劇的に改善したサービス…</p></div></article>
      <article class="article-card"><div class="article-thumb"><div class="photo" role="img" aria-label="2015年のサービスを表す写真"></div><span class="tag client">クライアントサイド</span></div>
        <div class="article-body"><time>2014.4.21</time><h2>2015年おすすめサービスまとめ</h2><p>こんにちはクライアントサイド担当Bです。今日は私的に気になるサービスについてまとめてみました。作業効率が劇的に改善したサービス…</p></div></article>
      <article class="article-card"><div class="article-thumb"><div class="photo" role="img" aria-label="2015年のサービスを表す写真"></div><span class="tag server">サーバーサイド</span></div>
        <div class="article-body"><time>2014.4.21</time><h2>2015年おすすめサービスまとめ</h2><p>こんにちはクライアントサイド担当Bです。今日は私的に気になるサービスについてまとめてみました。作業効率が劇的に改善したサービス…</p></div></article>
      <article class="article-card"><div class="article-thumb"><div class="photo" role="img" aria-label="2015年のサービスを表す写真"></div><span class="tag server">サーバーサイド</span></div>
        <div class="article-body"><time>2014.4.21</time><h2>2015年おすすめサービスまとめ</h2><p>こんにちはクライアントサイド担当Bです。今日は私的に気になるサービスについてまとめてみました。作業効率が劇的に改善したサービス…</p></div></article>
    </div>
    <a class="more-button">記事をもっと見る</a>
  </main>

  <aside class="sidebar">
    <div class="recruit-banner">
      <div class="logo-area"><span class="brand-mark"></span><span class="brand-name">ミラボルト テクノサービス</span></div>
      <div class="cta">採用情報はこちら</div>
    </div>

    <section class="pickup">
      <h4 class="pickup-title"><i></i>PICK UP<i></i></h4>
      <div class="pickup-item"><div class="pickup-thumb" role="img" aria-label="負荷分散のイラスト"></div><span>パフォーマンス改善！負荷分散をはじめよう</span></div>
      <div class="pickup-item"><div class="pickup-thumb" role="img" aria-label="負荷分散のイラスト"></div><span>パフォーマンス改善！負荷分散をはじめよう</span></div>
      <div class="pickup-item"><div class="pickup-thumb" role="img" aria-label="負荷分散のイラスト"></div><span>パフォーマンス改善！負荷分散をはじめよう</span></div>
      <div class="pickup-item"><div class="pickup-thumb" role="img" aria-label="負荷分散のイラスト"></div><span>パフォーマンス改善！負荷分散をはじめよう</span></div>
      <div class="pickup-item"><div class="pickup-thumb" role="img" aria-label="負荷分散のイラスト"></div><span>パフォーマンス改善！負荷分散をはじめよう</span></div>
    </section>

    <section class="categories">
      <h4>カテゴリー</h4>
      <ul>
        <li>すべて</li>
        <li>入門記事</li>
        <li>クライアントサイド</li>
        <li>サーバーサイド</li>
        <li>DB</li>
      </ul>
    </section>

    <div class="search">
      <div class="field"></div>
      <div class="button"><svg width="22" height="22" viewBox="0 0 22 22"><circle cx="9" cy="9" r="6.5" stroke="#fff" stroke-width="2.5" fill="none"/><path d="M14 14l6 6" stroke="#fff" stroke-width="3"/></svg></div>
    </div>
  </aside>
</div>

<footer class="site-footer">
  <div class="brand"><span class="brand-mark"></span><span class="brand-name">ミラボルト テクノサービス</span></div>
  <nav class="footer-nav"><span>FOOTER</span><span>FOOTER</span><span>FOOTER</span></nav>
</footer>

</body>
</html>
```